IT Support Business needs a Flyer Designed

Have just had new logo and business cards made for new business called Byte Harbor, am now in need of a new flyer design. Byte Harbor will be providing home and small business it support.
Updates
Byte Harbor flyer design brief has been uploaded. The contest has also been changed to payment guaranteed.
If you need anymore information please feel free to contact myself.
Project Deadline Extended
Reason: I signed up early to take advantage of the artforge 24 hour sale, and was a few days late in providing a design brief. Therefore I am extending the deadline by 2 days, to ensure it lasts for a good 2 weeks.
Have worked on and refined the Design Brief a bit more, hoping it makes it a bit clearer as to what I want on the flyer. If you have any questions please do not hesitate to ask.
I have refined the design brief overnight, after receiving some feedback, please refer to newly uploaded file for this morning. I am hoping it makes things clearer and easier.
Industry/Entity Type
Small Business

```html
<!DOCTYPE html>
<html lang="en">
<head>
<meta charset="utf-8">
<title>Byte Harbor – Tri-fold Brochure</title>
<link href="https://fonts.googleapis.com/css2?family=Open+Sans:wght@400;600&family=PT+Serif:ital,wght@0,400;0,700;1,400&display=swap" rel="stylesheet">
<style>
:root{
  --stage-top:#2f4a66;
  --stage-bottom:#101c2a;
  --pink:#e8185f;
  --pink-deep:#d9125a;
  --cream:#fcf9f1;
  --charcoal:#2b2b2b;
  --ink:#1e1e1e;
  --body:#3a3a3a;
  --accent-red:#9e2234;
  --brand-blue:#2f6fd8;
  --muted:#9a9a9a;
  --white:#ffffff;
}
*{margin:0;padding:0;box-sizing:border-box}
html,body{width:1200px;height:900px;overflow:hidden}
body{
  background:radial-gradient(ellipse at 50% 35%,var(--stage-top) 0%,var(--stage-bottom) 100%);
  font-family:"PT Serif",Georgia,serif;
  position:relative;
}
.sheet{position:absolute;display:flex;box-shadow:0 6px 18px rgba(0,0,0,.55)}
.sheet--outside{left:82px;top:45px;width:590px;height:378px}
.sheet--inside{left:543px;top:462px;width:590px;height:374px}
.panel{position:relative;height:100%}
.panel--pink{width:182px;background:var(--pink)}
.panel--cream{background:var(--cream)}
.panel--dark{background:var(--charcoal)}
.sheet--outside .panel--cream{width:222px}
.sheet--outside .panel--dark{width:186px}
.sheet--inside .panel--cream:first-child{width:205px}
.sheet--inside .panel--dark{width:187px}
.sheet--inside .panel--cream:last-child{width:198px}

.photo{position:absolute;display:block}
.photo--night{background:linear-gradient(90deg,#3b3a48 0%,#8a7f8e 30%,#c9b76a 50%,#4a4650 70%,#2d3140 100%)}
.photo--mall{background:linear-gradient(180deg,#c8ccd2 0%,#6f6a66 55%,#3a3532 100%)}
.photo--shop{background:linear-gradient(90deg,#2e2a28 0%,#5d5954 45%,#8fb48a 75%,#d9d3cf 100%)}

.section-head{position:absolute}
.section-head::before{content:"";position:absolute;left:-14px;top:3px;width:3px;height:29px;background:var(--accent-red)}
.section-title{font-family:"Open Sans",Arial,sans-serif;font-weight:400;font-size:22px;line-height:22px;color:var(--ink)}
.section-sub{font-family:"Open Sans",Arial,sans-serif;font-size:9.5px;letter-spacing:1.2px;color:var(--ink);margin-top:2px}
.panel--pink .section-title{color:var(--white)}
.panel--pink .section-head::before{background:var(--ink)}

.copy{position:absolute;font-size:7.4px;line-height:10px;color:var(--body)}
.copy b{color:var(--ink)}
.panel--pink .copy,.panel--pink .copy b{color:var(--white)}
.panel--dark .copy,.panel--dark .copy b{color:var(--white)}

.brand{position:absolute;font-family:"Open Sans",Arial,sans-serif;font-weight:600;font-size:17px;color:var(--brand-blue);white-space:nowrap;letter-spacing:.5px}

.brand-card{position:absolute;left:78px;top:146px;width:126px;height:66px;background:var(--charcoal);text-align:center}
.brand-card .brand{position:static;display:block;font-size:14px;margin-top:12px}
.brand-card .tagline{font-family:"Open Sans",Arial,sans-serif;font-size:8.5px;letter-spacing:.8px;color:var(--accent-red);margin-top:6px}

.info-title{position:absolute;left:79px;top:232px;font-family:"Open Sans",Arial,sans-serif;font-size:10px;letter-spacing:1.2px;color:var(--accent-red)}
.info-line{position:absolute;left:79px;font-size:6.4px;color:var(--ink)}
.info-line--red{color:var(--accent-red)}
.web-small{position:absolute;font-size:6.4px;color:var(--muted);width:100%;text-align:center}

.item{position:absolute;display:flex;gap:3px}
.item-num{font-family:"Open Sans",Arial,sans-serif;font-size:21px;line-height:20px;color:var(--ink);width:11px}
.item .copy{position:static;padding-top:2px}

.story-card{position:absolute;left:67px;top:146px;width:120px;height:64px;background:var(--white);border-left:3px solid var(--accent-red);padding:14px 0 0 10px}
.story-card .section-title{font-size:20px;line-height:20px}
.story-card .story-sub{font-family:"Open Sans",Arial,sans-serif;font-size:9.5px;letter-spacing:1.2px;color:var(--accent-red);margin-top:2px}
.quote{position:absolute;left:18px;width:151px;text-align:center;font-style:italic;font-size:7.4px;line-height:10px;color:#d8d8d8}
</style>
</head>
<body>

<section class="sheet sheet--outside">
  <div class="panel panel--pink">
    <div class="section-head" style="left:16px;top:18px">
      <h2 class="section-title">ABOUT-</h2>
      <p class="section-sub">YOUR SUBTITLE</p>
    </div>
    <p class="copy" style="left:26px;top:55px;width:144px"><b>Lorem ipsum dolor sit amet,</b> consectetur adipisicing elit, sed do eiusmod tempor incididunt ut labore et dolore magna aliqua. Ut enim ad minim veniam, quis nostrud exercitation ullamco laboris nisi ut aliquip ex ea commodo consequat.</p>
    <span class="photo photo--night" role="img" aria-label="Motion-blurred city street at night with passers-by" style="left:0;top:128px;width:182px;height:107px"></span>
    <div class="section-head" style="left:16px;top:250px">
      <h2 class="section-title">OBJEC-</h2>
      <p class="section-sub">YOUR SUBTITLE</p>
    </div>
    <p class="copy" style="left:26px;top:288px;width:144px"><b>Sed ut perspiciatis unde</b> omnis iste natus error sit voluptatem accusantium doloremque laudantium, totam rem aperiam, eaque ipsa quae ab illo inventore veritatis et quasi architecto beatae vitae dicta sunt explicabo.</p>
  </div>

  <div class="panel panel--cream">
    <div class="brand-card">
      <span class="brand">Byte Harbor</span>
      <p class="tagline">YOUR SUBTITLE HERE!</p>
    </div>
    <h3 class="info-title">YOUR INFO</h3>
    <p class="info-line" style="top:257px">Sed ut perspiciatis unde omnis iste natus</p>
    <p class="info-line" style="top:267px">411 Lorem Ipsum</p>
    <p class="info-line" style="top:277px">Magna OG 72458 <b>Country</b></p>
    <p class="info-line" style="top:297px">+ 00 555 014 2290</p>
    <p class="info-line info-line--red" style="top:317px">hello@byteharbor.net</p>
    <p class="info-line" style="top:347px">www.byteharbor.net</p>
  </div>

  <div class="panel panel--dark">
    <span class="brand" style="left:33px;top:50px">Byte Harbor</span>
    <span class="photo photo--night" role="img" aria-label="Motion-blurred city street at night with a walking figure" style="left:0;top:128px;width:186px;height:107px"></span>
    <p class="web-small" style="top:347px">www.byteharbor.net</p>
  </div>
</section>

<section class="sheet sheet--inside">
  <div class="panel panel--cream">
    <div class="section-head" style="left:16px;top:18px">
      <h2 class="section-title">SER-</h2>
      <p class="section-sub">YOUR SUBTITLE</p>
    </div>
    <div class="item" style="left:16px;top:68px">
      <span class="item-num">1</span>
      <p class="copy" style="width:165px"><b>Lorem ipsum dolor sit amet,</b> consectetur adipisicing elit, sed do eiusmod tempor incididunt ut labore et dolore magna aliqua. Ut enim ad minim veniam.</p>
    </div>
    <span class="photo photo--mall" role="img" aria-label="Busy shopping mall interior with shoppers" style="left:0;top:146px;width:187px;height:64px"></span>
    <div class="item" style="left:16px;top:232px">
      <span class="item-num">2</span>
      <p class="copy" style="width:165px"><b>Lorem ipsum dolor sit amet,</b> consectetur adipisicing elit, sed do eiusmod tempor.</p>
    </div>
    <div class="item" style="left:16px;top:275px">
      <span class="item-num">3</span>
      <p class="copy" style="width:165px"><b>Lorem ipsum dolor sit amet,</b> consectetur adipisicing elit, sed do eiusmod tempor incididunt ut labore et dolore magna aliqua. Ut enim ad minim veniam.</p>
    </div>
  </div>

  <div class="panel panel--dark">
    <span class="brand" style="left:33px;top:51px">Byte Harbor</span>
    <span class="photo photo--mall" role="img" aria-label="Bright shopping centre concourse with people walking" style="left:0;top:127px;width:187px;height:107px"></span>
    <div class="story-card">
      <h2 class="section-title">COM-</h2>
      <p class="story-sub">SHORT STORY</p>
    </div>
    <p class="copy" style="left:22px;top:249px;width:150px"><b>Lorem ipsum dolor sit amet,</b> consectetur adipisicing elit, sed do eiusmod tempor incididunt ut labore et dolore magna aliqua. Ut enim ad minim veniam.</p>
    <p class="quote" style="top:297px">Sed ut perspiciatis unde omnis iste natus error sit voluptatem accusantium.</p>
    <p class="web-small" style="top:333px;color:var(--accent-red)">hello@byteharbor.net</p>
    <p class="web-small" style="top:349px">www.byteharbor.net</p>
  </div>

  <div class="panel panel--cream">
    <div class="section-head" style="left:24px;top:18px">
      <h2 class="section-title">BEN-</h2>
      <p class="section-sub">YOUR SUBTITLE</p>
    </div>
    <div class="item" style="left:24px;top:68px">
      <span class="item-num">1</span>
      <p class="copy" style="width:160px"><b>Lorem ipsum dolor sit amet,</b> consectetur adipisicing elit, sed do eiusmod tempor incididunt ut labore et dolore magna aliqua. Ut enim ad minim veniam.</p>
    </div>
    <span class="photo photo--shop" role="img" aria-label="Shoppers browsing a clothing store" style="left:17px;top:146px;width:181px;height:64px"></span>
    <div class="item" style="left:24px;top:232px">
      <span class="item-num">2</span>
      <p class="copy" style="width:160px"><b>Lorem ipsum dolor sit amet,</b> consectetur adipisicing elit, sed do eiusmod tempor.</p>
    </div>
    <div class="item" style="left:24px;top:275px">
      <span class="item-num">3</span>
      <p class="copy" style="width:160px"><b>Lorem ipsum dolor sit amet,</b> consectetur adipisicing elit, sed do eiusmod tempor incididunt ut labore et dolore magna aliqua. Ut enim ad minim veniam.</p>
    </div>
  </div>
</section>

</body>
</html>
```